MINIMAL Design Alteration for a UI/UX design

- Below is the Sketch file as well the logo for a UI/UX infrustructure for an application that enables users to book instant cleaning services. However when it was started the project enabled users to book a wide variety of services. The logo includes a mop as well as a hammer. We want the designer to do the following two small edits on the platform. Them being :
1. Edit the logo as to include the mop and another symbol of cleaning in a visually appealing manner
2. Modify the UI/UX screen in the sketch file removing the other services and only maintaining the cleaning option in A VISUALLY APPEALING MANNER
Any useful edits would be appreciated !

best

Requirements
Must have
• ABILITY TO BOOK CLEANING SERVICE ONLY IN A APPEALING MANNER

```html
<!DOCTYPE html>
<html lang="en">
<head>
<meta charset="utf-8">
<title>Dashboard – Cleaning Reservations</title>
<link rel="stylesheet" href="https://fonts.googleapis.com/css2?family=Roboto:wght@300;400;500&display=swap">
<style>
  :root{
    --ink:#1f1f1f;
    --ink-soft:#3a3a3a;
    --muted:#9a9a9a;
    --blue:#2e9fe0;
    --green:#28b463;
    --line:#e2e2e2;
    --white:#ffffff;
    --mint-top:#f7fcfb;
    --mint:#e3f6f1;
    --lime:#f1fae3;
    --tab-bg:#fbfbfb;
    --tab-ink:#8a8a8a;
    --icon-grey:#7d8a92;
    --icon-red:#e2574c;
    --icon-orange:#f3b21f;
  }
  *{box-sizing:border-box;margin:0;padding:0}
  html,body{width:675px;height:1200px;overflow:hidden}
  body{font-family:"Roboto",Helvetica,Arial,sans-serif;color:var(--ink);background:var(--white);position:relative}
  .status-bar{position:absolute;top:0;left:0;width:675px;height:36px;font-size:22px;font-weight:500;display:flex;align-items:center;justify-content:space-between;padding:0 12px;background:var(--mint-top)}
  .status-bar .carrier{display:flex;align-items:center;gap:8px}
  .status-bar .time{position:absolute;left:0;right:0;text-align:center}
  .status-bar .battery{display:flex;align-items:center;gap:6px}
  .nav-bar{position:absolute;top:36px;left:0;width:675px;height:86px;display:flex;align-items:center;justify-content:center;font-size:29px;font-weight:400;background:var(--mint-top);border-bottom:1px solid var(--line)}
  .hero{position:absolute;top:122px;left:0;width:675px;height:319px;background:linear-gradient(180deg,var(--white) 0%,var(--mint) 100%)}
  .summary-card{position:absolute;top:22px;left:20px;width:635px;height:198px;background:var(--white);border-radius:6px;box-shadow:0 2px 14px rgba(0,0,0,.09)}
  .summary-art{position:absolute;left:34px;top:36px;width:126px;height:117px;border-radius:12px;background:linear-gradient(135deg,#dfe6ea,#b9c6cd)}
  .summary-title{position:absolute;left:194px;top:34px;font-size:32px;font-weight:500;line-height:43px;color:var(--ink-soft)}
  .summary-sub{position:absolute;left:194px;top:126px;font-size:25px;color:var(--muted)}
  .summary-sub .sep{margin:0 8px;font-size:18px;vertical-align:middle}
  .section-title{position:absolute;left:25px;top:255px;font-size:27px;font-weight:500;color:var(--ink-soft)}
  .reservation-list{position:absolute;top:441px;left:0;width:675px;list-style:none;border-top:1px solid var(--line)}
  .reservation{position:relative;height:140px;border-bottom:1px solid var(--line)}
  .reservation .status-dot{position:absolute;left:30px;top:25px;width:18px;height:18px;border-radius:50%;background:var(--green)}
  .reservation .service{position:absolute;left:63px;top:16px;font-size:27px;color:var(--ink)}
  .reservation .when{position:absolute;left:30px;top:58px;font-size:22px;color:var(--blue)}
  .reservation .address{position:absolute;left:30px;top:92px;font-size:21px;color:var(--muted)}
  .date-tile{position:absolute;left:549px;top:13px;width:108px;height:111px;border:1.5px solid #cfcfcf;background:var(--white);text-align:center}
  .date-tile::before,.date-tile::after{content:"";position:absolute;top:-8px;width:6px;height:14px;border:1.5px solid #cfcfcf;border-radius:3px;background:var(--white)}
  .date-tile::before{left:14px}.date-tile::after{right:14px}
  .date-tile .day{display:block;margin-top:18px;font-size:17px;color:var(--ink-soft)}
  .date-tile .num{display:block;font-size:30px;color:var(--blue);line-height:38px}
  .date-tile .month{display:block;font-size:17px;color:var(--ink-soft)}
  .add-reservation{position:absolute;left:30px;top:910px;display:flex;align-items:center;gap:14px;font-size:25px;color:var(--blue)}
  .footer-fade{position:absolute;top:999px;left:0;width:675px;height:113px;border-top:1px solid var(--line);background:linear-gradient(180deg,var(--white),var(--lime))}
  .tab-bar{position:absolute;top:1112px;left:0;width:675px;height:88px;background:var(--tab-bg);border-top:1px solid var(--line);display:flex}
  .tab{flex:1;display:flex;flex-direction:column;align-items:center;justify-content:flex-end;padding-bottom:8px;gap:8px;font-size:18px;color:var(--tab-ink)}
  .tab.active{color:var(--blue)}
  .tab svg{width:38px;height:38px}
  .app-mark{width:34px;height:34px;border-radius:8px;background:var(--green)}
</style>
</head>
<body>
  <header class="status-bar">
    <div class="carrier">
      <svg width="90" height="14" viewBox="0 0 90 14"><g fill="#1f1f1f"><circle cx="7" cy="7" r="6"/><circle cx="22" cy="7" r="6"/><circle cx="37" cy="7" r="6"/><circle cx="52" cy="7" r="6"/></g><circle cx="67" cy="7" r="5.5" fill="none" stroke="#1f1f1f" stroke-width="1.5"/></svg>
      <span>Nimbus</span>
      <svg width="26" height="20" viewBox="0 0 26 20"><path d="M13 19 L2 7 A16 16 0 0 1 24 7 Z" fill="#1f1f1f"/></svg>
    </div>
    <div class="time">9:41 AM</div>
    <div class="battery">
      <span>100%</span>
      <svg width="46" height="20" viewBox="0 0 46 20"><rect x="1" y="1" width="38" height="18" rx="4" fill="none" stroke="#1f1f1f" stroke-width="2"/><rect x="4" y="4" width="32" height="12" rx="2" fill="#1f1f1f"/><rect x="41" y="6" width="3" height="8" rx="1" fill="#1f1f1f"/></svg>
    </div>
  </header>

  <nav class="nav-bar">Dashboard</nav>

  <section class="hero">
    <div class="summary-card">
      <div class="summary-art" role="img" aria-label="Illustration of a vacuum cleaner"></div>
      <h1 class="summary-title">You have 3 Cleaning<br>Reservations</h1>
      <p class="summary-sub">1 Today<span class="sep">•</span>2 Upcoming</p>
    </div>
    <h2 class="section-title">Upcoming Reservations</h2>
  </section>

  <ul class="reservation-list">
    <li class="reservation">
      <span class="status-dot"></span>
      <span class="service">Cleaning - House</span>
      <span class="when">Today at 09:00 AM</span>
      <span class="address">412 Alder Row Apt. 7, Fairhaven MA 02719</span>
      <div class="date-tile"><span class="day">Monday</span><span class="num">18th</span><span class="month">March</span></div>
    </li>
    <li class="reservation">
      <span class="status-dot"></span>
      <span class="service">Cleaning - House</span>
      <span class="when">Tuesday 19th March at 09:00 AM</span>
      <span class="address">412 Alder Row Apt. 7, Fairhaven MA 02719</span>
      <div class="date-tile"><span class="day">Tuesday</span><span class="num">19th</span><span class="month">March</span></div>
    </li>
    <li class="reservation">
      <span class="status-dot"></span>
      <span class="service">Cleaning - House</span>
      <span class="when">Thursday 21st March at 09:00 AM</span>
      <span class="address">412 Alder Row Apt. 7, Fairhaven MA 02719</span>
      <div class="date-tile"><span class="day">Thursday</span><span class="num">21st</span><span class="month">March</span></div>
    </li>
  </ul>

  <div class="add-reservation">
    <svg width="38" height="38" viewBox="0 0 38 38"><circle cx="19" cy="19" r="17" fill="none" stroke="#2e9fe0" stroke-width="2.5"/><path d="M19 10v18M10 19h18" stroke="#2e9fe0" stroke-width="2.5" stroke-linecap="round"/></svg>
    <span>Add another reservation</span>
  </div>

  <div class="footer-fade"></div>

  <footer class="tab-bar">
    <div class="tab active"><span class="app-mark"></span><span>Dashboard</span></div>
    <div class="tab">
      <svg viewBox="0 0 38 38"><circle cx="19" cy="13" r="8" fill="#f3b21f"/><path d="M4 36c0-9 7-14 15-14s15 5 15 14z" fill="#5a8fbf"/></svg>
      <span>Account</span>
    </div>
    <div class="tab">
      <svg viewBox="0 0 38 38"><rect x="3" y="6" width="32" height="29" rx="3" fill="#ffffff" stroke="#c9c9c9" stroke-width="1.5"/><rect x="3" y="6" width="32" height="9" rx="3" fill="#e2574c"/><g fill="#e2574c"><rect x="9" y="19" width="5" height="4"/><rect x="17" y="19" width="5" height="4"/><rect x="25" y="19" width="5" height="4"/><rect x="9" y="26" width="5" height="4"/><rect x="17" y="26" width="5" height="4"/></g><rect x="10" y="2" width="3" height="8" rx="1" fill="#7d8a92"/><rect x="25" y="2" width="3" height="8" rx="1" fill="#7d8a92"/></svg>
      <span>Reservation</span>
    </div>
    <div class="tab">
      <svg viewBox="0 0 38 38"><path d="M19 4c-7 0-11 5-11 12v8l-4 5h30l-4-5v-8c0-7-4-12-11-12z" fill="#f3b21f"/><circle cx="19" cy="32" r="4" fill="#e09a12"/></svg>
      <span>Notification</span>
    </div>
    <div class="tab">
      <svg viewBox="0 0 38 38"><circle cx="19" cy="19" r="16" fill="#7d8a92"/><g fill="#ffffff"><circle cx="11" cy="19" r="2.5"/><circle cx="19" cy="19" r="2.5"/><circle cx="27" cy="19" r="2.5"/></g></svg>
      <span>More</span>
    </div>
  </footer>
</body>
</html>
```